Endocrinologist needs new stationery

I have a logo from MarkForge and now need stationery with the new logo.

Address: Suite 4, 282 Falcon Street, Richmond, VIC 3121
Phone: 03 9417 2253
Fax: 03 9417 2255
Website: www.drmaylacorwen.com.au
Email: admin@drmaylacorwen.com.au

```html
<!DOCTYPE html>
<html lang="en">
<head>
<meta charset="utf-8">
<title>Dr Mayla Corwen – Stationery Suite</title>
<link href="https://fonts.googleapis.com/css2?family=Libre+Baskerville&family=Open+Sans:wght@400;600&display=swap" rel="stylesheet">
<style>
  :root{
    --navy:#244a8a;
    --mauve:#9a6b8f;
    --paper:#f7f7f8;
    --backdrop:#e8e8ea;
    --ink:#2b2f3a;
    --wave-soft:#c3cde3;
    --serif:"Libre Baskerville", Georgia, serif;
    --sans:"Open Sans", Arial, sans-serif;
  }
  *{box-sizing:border-box;margin:0;padding:0}
  html,body{width:1200px;height:800px;overflow:hidden}
  body{background:var(--backdrop);position:relative;font-family:var(--sans);color:var(--ink)}
  .piece{position:absolute;overflow:hidden;box-shadow:0 2px 6px rgba(0,0,0,.12)}
  .piece--paper{background:var(--paper)}
  .piece--navy{background:var(--navy)}
  .brand-name{font-family:var(--serif);font-weight:400;color:var(--navy);white-space:nowrap;position:absolute}
  .brand-name--light{color:#fff}
  .wave-area{position:absolute}
  .contact-list{position:absolute;list-style:none}
  .contact-list li{display:flex;align-items:flex-start;gap:10px;line-height:1.4}
  .contact-list svg{flex:none;fill:var(--navy);margin-top:1px}

  /* Letterhead */
  .letterhead{left:22px;top:12px;width:439px;height:492px}
  .letterhead .brand-name{left:38px;top:58px;font-size:23px}
  .letterhead .wave-area{right:0;top:0;width:110px;height:110px;background:radial-gradient(ellipse at top right,var(--wave-soft) 0%,rgba(195,205,227,0) 70%)}
  .letterhead .contact-list{left:38px;top:358px;font-size:8.6px}
  .letterhead .contact-list li{margin-bottom:7px}
  .letterhead .swoosh{position:absolute;left:0;bottom:0}

  /* Business card front */
  .card-front{left:481px;top:29px;width:261px;height:143px}
  .card-front .brand-name{left:0;right:0;text-align:center;top:58px;font-size:18px}

  /* Business card back */
  .card-back{left:481px;top:194px;width:261px;height:169px}
  .card-back .card-name{position:absolute;left:19px;top:27px;font-family:var(--serif);font-size:13.5px;color:var(--navy)}
  .card-back .card-title{position:absolute;left:19px;top:47px;font-family:var(--serif);font-size:9.5px;color:var(--mauve)}
  .card-back .card-rule{position:absolute;left:19px;top:64px;width:126px;height:1px;background:var(--mauve)}
  .card-back .contact-list{left:19px;top:76px;font-size:7.6px;font-weight:600}
  .card-back .contact-list li{margin-bottom:3px}

  /* Compliment slip */
  .comp-slip{left:784px;top:30px;width:393px;height:218px}
  .comp-slip .brand-name{left:20px;top:34px;font-size:17px}
  .comp-slip .wave-area{left:0;bottom:0;width:110px;height:100px;background:radial-gradient(ellipse at bottom left,var(--wave-soft) 0%,rgba(195,205,227,0) 70%)}
  .comp-slip .address-block{position:absolute;left:250px;top:164px;padding-left:10px;border-left:1px solid var(--mauve);font-size:8.6px;line-height:1.55}

  /* Envelope */
  .envelope{left:784px;top:271px;width:392px;height:152px}
  .envelope .flap{position:absolute;left:0;top:0}
  .envelope .brand-name{left:0;right:0;text-align:center;top:33px;font-size:17px}

  /* Presentation card */
  .folder{left:19px;top:520px;width:432px;height:252px}
  .folder .panel{position:absolute;left:0;top:0}
  .folder .brand-name{left:32px;top:112px;font-size:21px}
  .folder .wave-area{right:0;bottom:0;width:200px;height:150px;background:radial-gradient(ellipse at bottom right,var(--wave-soft) 0%,rgba(195,205,227,0) 70%)}

  /* Prescription pad */
  .rx-pad{left:478px;top:391px;width:249px;height:379px}
  .rx-pad .brand-name{left:28px;top:38px;font-size:16px}
  .rx-field{position:absolute;font-size:8px;display:flex;align-items:flex-end;gap:5px}
  .rx-field .fill-line{display:block;height:1px;background:#555;margin-bottom:2px}
  .rx-symbol{position:absolute;left:20px;top:138px;font-family:var(--serif);font-size:20px;color:var(--mauve)}
  .rx-pad .rx-rule{position:absolute;left:20px;right:20px;top:286px;height:1px;background:var(--mauve)}
  .rx-pad .contact-list{font-size:7px}
  .rx-pad .contact-list li{gap:8px;margin-bottom:4px}
  .rx-pad .contact-left{left:14px;top:302px}
  .rx-pad .contact-right{left:115px;top:325px}

  /* Notebook cover */
  .notebook{left:751px;top:441px;width:185px;height:322px}
  .notebook .brand-name{left:0;right:0;text-align:center;top:93px;font-size:15px}
  .notebook .wave-area{right:0;bottom:0;width:185px;height:190px;background:radial-gradient(ellipse at bottom right,rgba(195,205,227,.35) 0%,rgba(195,205,227,0) 70%)}
</style>
</head>
<body>

<svg width="0" height="0" style="position:absolute" aria-hidden="true">
  <defs>
    <symbol id="icon-pin" viewBox="0 0 10 10"><path d="M5 0a3.6 3.6 0 0 0-3.6 3.6C1.4 6.3 5 10 5 10s3.6-3.7 3.6-6.4A3.6 3.6 0 0 0 5 0zm0 5a1.3 1.3 0 1 1 0-2.6A1.3 1.3 0 0 1 5 5z"/></symbol>
    <symbol id="icon-phone" viewBox="0 0 10 10"><path d="M2 .5l1.6 2-1 1.2a6 6 0 0 0 3.7 3.7l1.2-1 2 1.6-.8 1.5C4.6 9.6.4 5.4.5 1.3z"/></symbol>
    <symbol id="icon-fax" viewBox="0 0 10 10"><path d="M2.5 0h5v2.5h-5zM0 3h10v4.5H8V6H2v1.5H0zM2.5 6.5h5V10h-5z"/></symbol>
    <symbol id="icon-web" viewBox="0 0 10 10"><path d="M5 0a5 5 0 1 0 0 10A5 5 0 0 0 5 0zm3.9 4.4H7.2a7.6 7.6 0 0 0-.9-3.2 4 4 0 0 1 2.6 3.2zM5 1c.5.6 1 1.8 1.1 3.4H3.9C4 2.8 4.5 1.6 5 1zM3.7 1.2a7.6 7.6 0 0 0-.9 3.2H1.1a4 4 0 0 1 2.6-3.2zM1.1 5.6h1.7a7.6 7.6 0 0 0 .9 3.2 4 4 0 0 1-2.6-3.2zM5 9c-.5-.6-1-1.8-1.1-3.4h2.2C6 7.2 5.5 8.4 5 9zm1.3-.2a7.6 7.6 0 0 0 .9-3.2h1.7a4 4 0 0 1-2.6 3.2z"/></symbol>
    <symbol id="icon-mail" viewBox="0 0 10 10"><path d="M0 2h10v6H0zm1 1v.3l4 2.4 4-2.4V3z"/></symbol>
  </defs>
</svg>

<!-- Letterhead -->
<section class="piece piece--paper letterhead" aria-label="Letterhead">
  <div class="wave-area" role="img" aria-label="Fine flowing line pattern in soft blue"></div>
  <div class="brand-name">Dr Mayla Corwen</div>
  <ul class="contact-list">
    <li><svg width="9" height="9"><use href="#icon-pin"/></svg><span>Suite 4, 282 Falcon Street,<br>Richmond, VIC 3121</span></li>
    <li><svg width="9" height="9"><use href="#icon-phone"/></svg><span>03 9417 2253</span></li>
    <li><svg width="9" height="9"><use href="#icon-fax"/></svg><span>03 9417 2255</span></li>
    <li><svg width="9" height="9"><use href="#icon-web"/></svg><span>www.drmaylacorwen.com.au</span></li>
    <li><svg width="9" height="9"><use href="#icon-mail"/></svg><span>admin@drmaylacorwen.com.au</span></li>
  </ul>
  <svg class="swoosh" width="439" height="80" viewBox="0 0 439 80" aria-hidden="true">
    <path d="M120 80 C230 76 340 50 439 22 L439 80 Z" fill="var(--navy)"/>
    <path d="M150 80 C260 72 360 44 439 15" fill="none" stroke="var(--mauve)" stroke-width="2.5"/>
  </svg>
</section>

<!-- Business card front -->
<section class="piece piece--navy card-front" aria-label="Business card front">
  <div class="brand-name brand-name--light">Dr Mayla Corwen</div>
</section>

<!-- Business card back -->
<section class="piece piece--paper card-back" aria-label="Business card back">
  <div class="card-name">Dr Mayla Corwen</div>
  <div class="card-title">Endocrinologist</div>
  <div class="card-rule"></div>
  <ul class="contact-list">
    <li><svg width="8" height="8"><use href="#icon-pin"/></svg><span>Suite 4, 282 Falcon Street,<br>Richmond, VIC 3121</span></li>
    <li><svg width="8" height="8"><use href="#icon-phone"/></svg><span>03 9417 2253</span></li>
    <li><svg width="8" height="8"><use href="#icon-fax"/></svg><span>03 9417 2255</span></li>
    <li><svg width="8" height="8"><use href="#icon-mail"/></svg><span>admin@drmaylacorwen.com.au</span></li>
    <li><svg width="8" height="8"><use href="#icon-web"/></svg><span>www.drmaylacorwen.com.au</span></li>
  </ul>
</section>

<!-- Compliment slip -->
<section class="piece piece--paper comp-slip" aria-label="Compliment slip">
  <div class="brand-name">Dr Mayla Corwen</div>
  <div class="wave-area" role="img" aria-label="Fine flowing line pattern in soft blue"></div>
  <div class="address-block">Suite 4, 282 Falcon Street,<br>Richmond, VIC 3121</div>
</section>

<!-- Envelope -->
<section class="piece piece--navy envelope" aria-label="Envelope">
  <svg class="flap" width="392" height="152" viewBox="0 0 392 152" aria-hidden="true">
    <path d="M0 0 L30 70 Q40 84 60 88 L196 104 L332 88 Q352 84 362 70 L392 0" fill="none" stroke="#1b3a70" stroke-width="1.2"/>
  </svg>
  <div class="brand-name brand-name--light">Dr Mayla Corwen</div>
</section>

<!-- Presentation card -->
<section class="piece piece--paper folder" aria-label="Presentation card">
  <div class="wave-area" role="img" aria-label="Fine flowing line pattern in soft blue"></div>
  <svg class="panel" width="432" height="252" viewBox="0 0 432 252" aria-hidden="true">
    <path d="M0 0 L222 0 C268 60 276 190 228 252 L0 252 Z" fill="var(--navy)"/>
    <path d="M226 0 C272 60 280 190 232 252" fill="none" stroke="var(--mauve)" stroke-width="3"/>
  </svg>
  <div class="brand-name brand-name--light">Dr Mayla Corwen</div>
</section>

<!-- Prescription pad -->
<section class="piece piece--paper rx-pad" aria-label="Prescription pad">
  <div class="brand-name">Dr Mayla Corwen</div>
  <div class="rx-field" style="left:20px;top:84px"><span>Name:</span><span class="fill-line" style="width:106px"></span></div>
  <div class="rx-field" style="left:160px;top:84px"><span>Date:</span><span class="fill-line" style="width:44px"></span></div>
  <div class="rx-field" style="left:20px;top:104px"><span>Address:</span><span class="fill-line" style="width:172px"></span></div>
  <div class="rx-symbol">Rx</div>
  <div class="rx-rule"></div>
  <ul class="contact-list contact-left">
    <li><svg width="7" height="7"><use href="#icon-pin"/></svg><span>Suite 4, 282 Falcon Street,<br>Richmond, VIC 3121</span></li>
    <li><svg width="7" height="7"><use href="#icon-phone"/></svg><span>03 9417 2253</span></li>
    <li><svg width="7" height="7"><use href="#icon-fax"/></svg><span>03 9417 2255</span></li>
  </ul>
  <ul class="contact-list contact-right">
    <li><svg width="7" height="7"><use href="#icon-web"/></svg><span>www.drmaylacorwen.com.au</span></li>
    <li><svg width="7" height="7"><use href="#icon-mail"/></svg><span>admin@drmaylacorwen.com.au</span></li>
  </ul>
</section>

<!-- Notebook cover -->
<section class="piece piece--navy notebook" aria-label="Notebook cover">
  <div class="wave-area" role="img" aria-label="Fine flowing line pattern in pale blue"></div>
  <div class="brand-name brand-name--light">Dr Mayla Corwen</div>
</section>

</body>
</html>
```